Velkaris Crosses

Morrow Designs is a growing wedding ring wholesaler/manufacturer based in NYC. We have recently teamed up with a cross designer from Greece and added their line of cross pendants to our product line. We would like to introduce the product to our customers. We are looking for a clean looking postcard. Is it possible to remove the style number and weights from the bottom right corner of each image?
We will provide wording, etc. upon request.

Thanks.
Updates

We would like all or most images to be on the postcard, front and back is fine. Thanks!!

Industry/Entity Type

Wedding

```html
<!DOCTYPE html>
<html lang="en">
<head>
<meta charset="utf-8">
<title>Velkaris Crosses – Postcard</title>
<link rel="stylesheet" href="https://fonts.googleapis.com/css2?family=Sorts+Mill+Goudy&family=Cormorant+Garamond:wght@500&display=swap">
<style>
  :root {
    --page-bg: #e4e3e1;
    --card-light: #fbfafa;
    --card-mid: #dcd8d6;
    --card-edge: #b5acaa;
    --ink: #2b2422;
    --ink-soft: #4a403d;
    --deco: rgba(150, 132, 128, 0.35);
    --logo-band: rgba(188, 170, 160, 0.55);
    --rule: #cfc8c5;
    --gold-hi: #f7d63a;
    --gold-lo: #c99a05;
    --silver-hi: #f3f3f3;
    --silver-lo: #a7a7a7;
  }
  * { margin: 0; padding: 0; box-sizing: border-box; }
  html, body { width: 900px; height: 1200px; overflow: hidden; }
  body {
    background: var(--page-bg);
    position: relative;
    font-family: "Sorts Mill Goudy", "Cormorant Garamond", serif;
    color: var(--ink);
  }
  .postcard {
    position: absolute;
    overflow: hidden;
    background: radial-gradient(circle at var(--glow-x) var(--glow-y), var(--card-light) 0%, #eeebea 22%, var(--card-mid) 60%, var(--card-edge) 100%);
  }
  .postcard--front { left: 78px; top: 35px; width: 746px; height: 577px; --glow-x: 68%; --glow-y: 26%; }
  .postcard--back  { left: 78px; top: 627px; width: 598px; height: 463px; --glow-x: 58%; --glow-y: 27%;
    background: radial-gradient(circle at 58% 27%, var(--card-light) 0%, #f1efee 25%, #dedad8 65%, #cbc3c1 100%); }

  .brand-deco {
    position: absolute;
    font-family: "Cormorant Garamond", serif;
    font-weight: 500;
    color: var(--deco);
    font-size: 20px;
    letter-spacing: 1px;
    white-space: nowrap;
  }
  .tagline {
    position: absolute;
    font-size: 18px;
    color: var(--ink);
    white-space: nowrap;
  }
  .brand-mark {
    position: absolute;
    display: flex;
    align-items: center;
    gap: 10px;
    padding: 0 12px;
    font-family: "Sorts Mill Goudy", serif;
    color: var(--ink);
    font-size: 25px;
    letter-spacing: 1px;
    text-transform: uppercase;
    white-space: nowrap;
  }
  .brand-mark__square { width: 30px; height: 30px; border: 2px solid var(--ink); flex: none; }
  .postcard--front .brand-mark { left: 35px; top: 518px; width: 238px; height: 56px; background: var(--logo-band); }
  .postcard--back .brand-mark { left: 56px; top: 4px; height: 43px; font-size: 21px; background: rgba(255,255,255,0.35); }
  .postcard--back .brand-mark__square { width: 25px; height: 25px; }

  .pendant { position: absolute; border-radius: 6px; }
  .pendant--gold { left: 328px; top: 176px; width: 164px; height: 293px; background: linear-gradient(100deg, var(--gold-lo), var(--gold-hi) 45%, var(--gold-lo)); }
  .pendant--silver { left: 551px; top: 182px; width: 162px; height: 281px; background: linear-gradient(100deg, var(--silver-lo), var(--silver-hi) 45%, var(--silver-lo)); }
  .pendant--ghost { left: 0; top: 158px; width: 74px; height: 287px; background: linear-gradient(90deg, rgba(255,255,255,0.35), rgba(200,195,193,0.25)); border-radius: 0 6px 6px 0; }

  .info { position: absolute; left: 51px; top: 238px; width: 234px; text-align: center; }
  .info__title { font-size: 14px; font-weight: normal; margin-bottom: 12px; color: var(--ink); }
  .info__body { font-size: 12px; line-height: 1.33; color: var(--ink-soft); }

  .address-lines { position: absolute; left: 305px; top: 0; width: 263px; height: 100%; }
  .address-lines span { position: absolute; left: 0; width: 100%; height: 1px; background: var(--rule); }
</style>
</head>
<body>

  <section class="postcard postcard--front" aria-label="Postcard front">
    <div class="brand-deco" style="left:64px; top:280px;">Velkaris Crosses</div>
    <p class="tagline" style="left:64px; top:308px;">Arrived from greece</p>
    <div class="pendant pendant--gold" role="img" aria-label="Yellow and white gold cross pendant with a row of stones"></div>
    <div class="pendant pendant--silver" role="img" aria-label="White gold cross pendant with a row of stones"></div>
    <div class="brand-mark"><span class="brand-mark__square"></span>Morrow Designs</div>
  </section>

  <section class="postcard postcard--back" aria-label="Postcard back">
    <div class="pendant pendant--ghost" role="img" aria-label="Faint cross pendant detail"></div>
    <div class="brand-mark"><span class="brand-mark__square"></span>Morrow Designs</div>
    <div class="brand-deco" style="left:140px; top:115px;">Velkaris Crosses</div>
    <p class="tagline" style="left:143px; top:150px; font-size:15px;">Arrived from greece</p>
    <div class="info">
      <h2 class="info__title">Information about new collection</h2>
      <p class="info__body">Lorem Ipsum is simply dummy text of the printing and typesetting industry. Lorem Ipsum has been the industry's standard dummy text ever since the 1500s, when an unknown printer took a galley of type and scrambled it to make a type specimen book.</p>
    </div>
    <div class="address-lines" aria-hidden="true">
      <span style="top:244px;"></span>
      <span style="top:275px;"></span>
      <span style="top:307px;"></span>
    </div>
  </section>

</body>
</html>
```